Mirvald Health & Wellness needs a fresh and interesting website

I need a rebrand and redevelopment of my website, www.tessapinlowe.com
Our mission is provide bespoke , lifestyle medicine , everyone has their own path to health. and we are creating a personalized experience for people to life their life to the fullest
Mirvald - means sea lands
I need an landing page and about page and potentially a few project launch pages , I have been using Wordpress for my basic information and then I use Kartra for the launch pages of my programs since I can edit those easily.

Target Market(s)

Corporate and individual's who are interested in a different perspective on health and wellness , and living with a chronic illness

Industry/Entity Type

Health, lifestyle , wellness coaching and medicine

Coding

Number of Pages Required

2 page

Font styles to use
Other font styles liked:
• look into the logo

Requirements
Must have
• the logo I uploaded
Nice to have
• I want a fresh perspective on health, I have bamboo, hibiscus vibes in my logo , but also like more of a water vibe/ I want something earthy but not too boho it needs to be clean
Should not have
• every other holistic health vibe,

```html
<!DOCTYPE html>
<html lang="en">
<head>
<meta charset="UTF-8">
<title>Mirvald Health &amp; Wellness</title>
<link rel="stylesheet" href="https://fonts.googleapis.com/css2?family=Tinos:wght@400&family=Outfit:wght@400;500;600&display=swap">
<style>
:root{
  --blue:#046a96;
  --blue-deep:#045b82;
  --green:#6bb000;
  --green-bright:#74b400;
  --ink:#1f1f1f;
  --muted:#6c6c6c;
  --white:#ffffff;
  --sky:#d9dde0;
}
*{box-sizing:border-box;margin:0;padding:0}
html,body{width:1200px;height:3600px;overflow:hidden}
body{position:relative;font-family:"Outfit",sans-serif;color:var(--ink);background:var(--white)}
.abs{position:absolute}
.serif{font-family:"Tinos",serif;font-weight:400}

/* hero */
.hero{left:0;top:0;width:1200px;height:684px;background:linear-gradient(180deg,#e6e7e6 0%,#cfd3d4 40%,#8a8f8c 70%,#6f6a5e 100%)}
.hero-word{left:0;top:190px;width:1200px;text-align:center;font-size:190px;letter-spacing:6px;color:rgba(255,255,255,.55)}
.nav-link{top:39px;font-size:14px;color:#2b2b2b}
.nav-link.active{color:var(--green)}
.nav-mark{left:143px;top:0;width:36px;height:3px;background:var(--green)}
.brand{left:500px;top:34px;width:200px;text-align:center;font-size:26px;color:var(--blue);letter-spacing:1px}
.social{top:35px;width:28px;height:28px;border-radius:50%;background:var(--white)}
.social::after{content:"";position:absolute;left:10px;top:10px;width:8px;height:8px;border-radius:50%;background:var(--blue)}
.btn{display:flex;align-items:center;justify-content:center;border-radius:30px;background:var(--green);color:var(--white);font-weight:600;text-transform:uppercase}
.quote{left:928px;top:34px;width:127px;height:32px;font-size:12px}
.badge{left:554px;top:638px;width:92px;height:92px;border-radius:50%;background:rgba(255,255,255,.55)}
.badge::after{content:"";position:absolute;left:12px;top:12px;width:68px;height:68px;border-radius:50%;background:var(--white)}

/* about */
.about{left:0;top:684px;width:1200px;height:519px;background:var(--blue)}
.about-title{left:143px;top:785px;font-size:31px;color:var(--white);letter-spacing:.3px}
.about-text{left:143px;width:540px;font-size:12.6px;line-height:20px;color:var(--white);text-align:justify}
.learn{left:143px;top:1051px;width:127px;height:33px;font-size:11.5px}
.portrait-ring{left:757px;top:784px;width:308px;height:308px;border-radius:50%;border:3px solid #e5eef2}
.portrait{left:772px;top:799px;width:278px;height:278px;border-radius:50%;background:radial-gradient(circle at 50% 40%,#9a9a9a,#3a3a3a 75%);border:6px solid #7aa9c2}

/* mission */
.bamboo-left{left:0;top:1203px;width:160px;height:819px;background:linear-gradient(90deg,#7fb82a,#b6dc54 50%,rgba(255,255,255,0))}
.bamboo-right{left:1040px;top:1203px;width:160px;height:660px;background:linear-gradient(270deg,#7fb82a,#b8dc5a 55%,rgba(255,255,255,0))}
.section-title{left:0;width:1200px;text-align:center;font-size:37px}
.mission-text{left:275px;top:1347px;width:650px;font-size:19.5px;line-height:28px;color:#3a3a3a;text-align:center}
.rule{left:423px;top:1493px;width:354px;height:4px;background:var(--green)}
.circle-photo{width:270px;height:270px;border-radius:50%;border:8px solid var(--green)}
.circle-label{width:270px;text-align:center;top:1874px;font-size:20px;font-weight:500}

/* target */
.target{left:0;top:2022px;width:1200px;height:653px;background:var(--green-bright)}
.target-photo{left:144px;top:2175px;width:455px;height:404px;background:linear-gradient(135deg,#f3f1ee,#ddd6cc 60%,#b9a58c)}
.card{left:557px;top:2218px;width:498px;height:313px;background:var(--white);border-left:17px solid var(--blue)}
.item-dot{width:38px;height:38px;border-radius:50%;border:2px solid var(--blue)}
.item-title{font-size:23px;color:var(--blue)}
.item-text{font-size:12.8px;line-height:20px;color:#6a6a6a;width:340px}
.divider{left:603px;top:2370px;width:422px;height:1px;background:#e3e3e3}

/* newsletter */
.field{top:2840px;height:46px;border-radius:30px;background:var(--white);box-shadow:0 2px 10px rgba(0,0,0,.09);font-size:12.5px;color:#6b6b6b;padding-left:29px;display:flex;align-items:center}
.subscribe{left:735px;top:2840px;width:243px;height:46px;font-size:13px}
.gallery{top:2955px;width:207px;height:190px}
.arrow{top:3040px;width:26px;height:26px}

/* footer */
.footer{left:0;top:3255px;width:1200px;height:345px;background:linear-gradient(180deg,#0a6c98 0%,#075e86 60%,#0a5a7d 100%)}
.foot-brand{left:150px;top:3400px;width:280px;text-align:center;font-size:46px;color:var(--white);letter-spacing:2px}
.foot-tag{left:150px;top:3455px;width:280px;text-align:center;font-size:13px;color:var(--white);letter-spacing:5px}
.foot-mark{left:263px;top:3340px;width:52px;height:52px;border-radius:50%;border:3px solid var(--white)}
.vline{top:3345px;width:1px;height:135px;background:rgba(255,255,255,.3)}
.foot-head{top:3330px;font-size:20px;font-weight:500;color:var(--white)}
.foot-link{left:569px;font-size:12.8px;color:var(--white)}
.contact-icon{left:829px;width:24px;height:24px;border-radius:50%;background:var(--white)}
.contact-text{left:868px;font-size:12.8px;color:var(--white)}
.copy{left:0;top:3535px;width:1200px;text-align:center;font-size:12.5px;color:var(--white)}
</style>
</head>
<body>

<!-- hero -->
<div class="abs hero" role="img" aria-label="Woman sitting on a mountain top with arms open above misty valleys"></div>
<div class="abs hero-word serif">MIRVALD</div>
<div class="abs nav-mark"></div>
<div class="abs nav-link active" style="left:143px">Home</div>
<div class="abs nav-link" style="left:212px">About</div>
<div class="abs nav-link" style="left:282px">Services</div>
<div class="abs nav-link" style="left:366px">Contact</div>
<div class="abs brand serif">MIRVALD</div>
<div class="abs social" style="left:810px"></div>
<div class="abs social" style="left:842px"></div>
<div class="abs social" style="left:874px"></div>
<div class="abs btn quote">Get a quote</div>

<!-- about -->
<section class="abs about"></section>
<div class="abs badge"></div>
<h2 class="abs about-title serif">DR TESSA P LINLOWE DACM, L.AC.</h2>
<p class="abs about-text" style="top:836px">At a young age, I discovered the transformative power of Eastern Medicine when it helped me overcome lung concerns, propelling me toward my dreams as a young athlete. Years later, I faced a pivotal choice: How could I best serve and heal my community? The answer was crystal clear—Eastern Medicine.</p>
<p class="abs about-text" style="top:935px">As an Eastern Medicine doctor, I've had the privilege of positively impacting my community through integrative health choices. My journey began after seven years of nurturing creativity and leadership in theatre costume design, when I made the life-altering decision to merge my love for art and science in the field of Acupuncture and Traditional East Asian Medicine (TEAM).</p>
<div class="abs btn learn">Learn more</div>
<div class="abs portrait-ring"></div>
<div class="abs portrait" role="img" aria-label="Black and white portrait of the doctor"></div>

<!-- mission -->
<div class="abs bamboo-left" role="img" aria-label="Green bamboo stalks and leaves"></div>
<div class="abs bamboo-right" role="img" aria-label="Green bamboo stalks and leaves"></div>
<h2 class="abs section-title serif" style="top:1290px">OUR MISSION</h2>
<p class="abs mission-text">Our mission is to provide bespoke , lifestyle medicine , everyone has their own path to health. and we are creating a personalized experience for people to live their life to the fullest.</p>
<div class="abs rule"></div>
<div class="abs circle-photo" style="left:145px;top:1588px;background:linear-gradient(135deg,#e8e2d8,#b9aa96 60%,#9a9fa8)" role="img" aria-label="Senior woman resting on an exercise ball"></div>
<div class="abs circle-photo" style="left:465px;top:1588px;background:linear-gradient(180deg,#d8dfe3,#b9c6cc 60%,#59636a)" role="img" aria-label="Hiker raising arms on a cliff"></div>
<div class="abs circle-photo" style="left:784px;top:1588px;background:linear-gradient(180deg,#9fb3c1,#34463d 35%,#6e8fa2 60%,#4d6b7c)" role="img" aria-label="Woman meditating on a rock in a lake"></div>
<div class="abs circle-label" style="left:145px">Lorem ipsum dolor</div>
<div class="abs circle-label" style="left:465px">Lorem ipsum dolor</div>
<div class="abs circle-label" style="left:784px">Lorem ipsum dolor</div>

<!-- target -->
<section class="abs target"></section>
<h2 class="abs section-title serif" style="top:2108px;color:var(--white)">OUR TARGET ARE</h2>
<div class="abs target-photo" role="img" aria-label="Woman stretching her neck at a desk beside wellness letter tiles"></div>
<div class="abs card"></div>
<div class="abs item-dot" style="left:603px;top:2248px"></div>
<div class="abs item-title serif" style="left:662px;top:2250px">Corporate</div>
<p class="abs item-text" style="left:662px;top:2290px">Lorem ipsum dolor sit amet, consectetur adipiscing elit, sed do eiusmod tempor incididunt ut labore et dolore elit, sed do eiusmod et dolore magna aliqua.</p>
<div class="abs divider"></div>
<div class="abs item-dot" style="left:603px;top:2384px"></div>
<div class="abs item-title serif" style="left:662px;top:2386px">Individual Person</div>
<p class="abs item-text" style="left:662px;top:2426px">Lorem ipsum dolor sit amet, consectetur adipiscing elit, sed do eiusmod tempor incididunt ut labore et dolore elit, sed do eiusmod et dolore magna aliqua.</p>

<!-- newsletter -->
<h2 class="abs section-title serif" style="top:2770px">KEEP UP WITH OUR NEWSLETTER</h2>
<div class="abs field" style="left:207px;width:243px">Name</div>
<div class="abs field" style="left:471px;width:243px">Email address</div>
<div class="abs btn subscribe">Subscribe</div>
<svg class="abs arrow" style="left:57px" viewBox="0 0 26 26"><path d="M16 5 L8 13 L16 21" fill="none" stroke="#1f1f1f" stroke-width="2.5"/></svg>
<div class="abs gallery" style="left:144px;background:linear-gradient(135deg,#8a6a4a,#c9a98a 50%,#e8e2d8)" role="img" aria-label="Woman breathing calmly outdoors"></div>
<div class="abs gallery" style="left:379px;background:linear-gradient(135deg,#c9d2cc,#8ea56e 55%,#4f5b45)" role="img" aria-label="Woman with headphones holding a water bottle"></div>
<div class="abs gallery" style="left:613px;background:linear-gradient(135deg,#7fb4c4,#d98d86 55%,#e6d2c2)" role="img" aria-label="Woman smiling in a bright kitchen"></div>
<div class="abs gallery" style="left:848px;background:linear-gradient(135deg,#a8c6dd,#5e7d54 55%,#9c7456)" role="img" aria-label="Woman enjoying the sun among trees"></div>
<svg class="abs arrow" style="left:1113px" viewBox="0 0 26 26"><path d="M10 5 L18 13 L10 21" fill="none" stroke="#1f1f1f" stroke-width="2.5"/></svg>

<!-- footer -->
<footer class="abs footer" role="img" aria-label="Calm water with smooth stones"></footer>
<div class="abs foot-mark"></div>
<div class="abs foot-brand serif">MIRVALD</div>
<div class="abs foot-tag serif">HEALTH &amp; WELLNESS</div>
<div class="abs vline" style="left:489px"></div>
<div class="abs vline" style="left:753px"></div>
<div class="abs foot-head" style="left:569px">Quick Links</div>
<div class="abs foot-link" style="top:3376px">Home</div>
<div class="abs foot-link" style="top:3396px">About</div>
<div class="abs foot-link" style="top:3416px">Services</div>
<div class="abs foot-link" style="top:3436px">Blog</div>
<div class="abs foot-link" style="top:3456px">Contact</div>
<div class="abs foot-head" style="left:827px">Contact</div>
<div class="abs contact-icon" style="top:3376px"></div>
<svg class="abs" style="left:835px;top:3380px" width="12" height="16" viewBox="0 0 12 16"><path d="M6 1a5 5 0 0 1 5 5c0 4-5 9-5 9S1 10 1 6a5 5 0 0 1 5-5z" fill="var(--green)"/><circle cx="6" cy="6" r="1.8" fill="#fff"/></svg>
<div class="abs contact-text" style="top:3379px">123, Lorem ipsum dolor</div>
<div class="abs contact-icon" style="top:3416px"></div>
<svg class="abs" style="left:835px;top:3422px" width="12" height="12" viewBox="0 0 12 12"><path d="M2 1l2.5 0 1 3-1.5 1a7 7 0 0 0 3 3l1-1.5 3 1V10a1.5 1.5 0 0 1-1.5 1.5A9.5 9.5 0 0 1 .5 2.5 1.5 1.5 0 0 1 2 1z" fill="var(--green)"/></svg>
<div class="abs contact-text" style="top:3419px">+1 888 888 8888</div>
<div class="abs contact-icon" style="top:3456px"></div>
<svg class="abs" style="left:835px;top:3463px" width="12" height="10" viewBox="0 0 12 10"><rect x="0.5" y="0.5" width="11" height="9" fill="var(--green)"/><path d="M0.5 0.5 L6 5 L11.5 0.5" fill="none" stroke="#fff" stroke-width="1"/></svg>
<div class="abs contact-text" style="top:3459px">info@companyname.com</div>
<div class="abs copy">© Copyrights 2024 | All Rights Reserved</div>

</body>
</html>
```